Folded Business Cards for Guarantee, Layaway & The Fine Print

I am looking for a set of (3) folded business for our guarantee, layaway and fine print policies. I would like the same design for each of these cards, with the exception of the picture, title and verbiage.
The front of each card must include our logo, the title of the card (Our Guarantee, Layaway or The Fine Print,) and a picture of a piece of jewelry. The inside of the card should state our policies. The back of the card should have our logo, address (Sandhollow Drive #9, Cedarfield, VT 03871,) phone # (603-555-0148) email & web address (info@kastonjewelry.example, www.kastonjewelry.example) and social media icons (FB, Twitter, Pinterest, Instagram)

The layaway card needs a place for the customer's signature.

I was thinking the orientation of the card should be vertical but if the right design ends up being horizontal, I'm ok with that. I do have concerns about readability and that this may be too much information for a folded business card. So, I am open to either changing the front & back, if need be or going to a different format (standard postcard size. Verbiage may also need to be trimmed down, but I need to know what is possible first.

Our branding colors are espresso brown & coppery orange so please do not stray from this color palette. The font of our logo is joefin. I would like the verbiage of the cards to be in quattrocento sans font. We would like a modern & clean look please.

Attached, please find our logo, policies and jewelry pictures. For picture placement, please do the following: Layaway Card (Quartz & onyx pendant,) The Fine Print Card (Orange Garnet Pendant,) Our Guarantee (triple Green Tourmaline Ring.)

```html
<!DOCTYPE html>
<html lang="en">
<head>
<meta charset="utf-8">
<title>Kaston Fine Jewelry – Policy Cards</title>
<link href="https://fonts.googleapis.com/css2?family=Quattrocento+Sans:wght@400&family=Yellowtail&display=swap" rel="stylesheet">
<style>
:root{
  --espresso:#5c3310;
  --copper:#c9732c;
  --cream:#ffffff;
  --page:#ffffff;
}
*{box-sizing:border-box;margin:0;padding:0}
html,body{width:1200px;height:1200px;overflow:hidden;background:var(--page)}
.canvas{position:relative;width:1200px;height:1200px}

.card{position:absolute;width:656px;height:560px;border:2px solid var(--espresso);background:var(--cream);overflow:hidden}
.mini{transform:scale(.5885);transform-origin:0 0}

/* brand name: set in the text face, one weight, one colour */
.brand{position:absolute;left:0;right:0;text-align:center;font-family:"Quattrocento Sans",sans-serif;font-weight:400}
.brand-name{display:block;font-size:50px;letter-spacing:8px;line-height:1}
.brand-tag{display:block;font-size:19px;letter-spacing:1px;margin-top:14px}

/* back panel */
.back-panel{position:absolute;left:0;top:0;width:328px;height:100%;background:var(--espresso);color:var(--cream)}
.back-panel .brand{top:58px;color:var(--copper)}
.contact-list{position:absolute;left:32px;top:188px;list-style:none;font-family:"Quattrocento Sans",sans-serif;font-size:16.5px;line-height:1.3}
.contact-list li{display:flex;align-items:center;min-height:43px}
.contact-list svg{width:26px;height:26px;flex:none;margin-right:10px}
.contact-list .address{align-items:flex-start;min-height:62px}

/* front panel */
.front-panel{position:absolute;left:328px;top:0;width:326px;height:100%}
.front-panel .brand{top:58px;color:var(--espresso)}
.title-band{position:absolute;left:0;right:0;top:170px;height:96px;border-top:6px solid var(--espresso);border-bottom:6px solid var(--espresso);background:var(--cream)}
.title-band h2{position:absolute;left:0;right:0;top:6px;height:70px;background:var(--espresso);color:var(--cream);font-family:"Yellowtail",cursive;font-weight:400;font-size:42px;text-align:center;line-height:70px}
.jewel{position:absolute;left:40px;right:40px;top:272px;bottom:14px}
.jewel-gold{background:radial-gradient(ellipse at 50% 62%,#d98a22 0,#d9a441 14%,#ecd39a 30%,var(--cream) 62%)}
.jewel-green{background:radial-gradient(ellipse at 50% 50%,#3f6b2c 0,#c9a23a 22%,#8a7f70 40%,var(--cream) 68%)}
.jewel-quartz{background:radial-gradient(ellipse at 50% 55%,#1f1713 0,#7a5a44 24%,#d9c3a4 42%,var(--cream) 68%)}

/* inside panel */
.inside{padding:22px 22px 0 22px;color:var(--espresso);font-family:"Quattrocento Sans",sans-serif;font-size:17px;line-height:1.32}
.inside h3{font-family:"Yellowtail",cursive;font-weight:400;font-size:27px;margin-bottom:12px}
.inside p{margin-bottom:20px}
.sign{position:absolute;right:22px;bottom:18px;text-align:right;color:var(--espresso);font-family:"Quattrocento Sans",sans-serif;font-weight:400}
.sign .s-name{display:block;font-size:26px;letter-spacing:4px;line-height:1}
.sign .s-tag{display:block;font-size:10px;margin-top:4px}
.inside-mini{padding-top:66px}
.inside-mini p{margin-bottom:20px}
.lead-guarantee{height:174px;overflow:hidden}
.lead-layaway{height:195px;overflow:hidden}
</style>
</head>
<body>
<svg width="0" height="0" style="position:absolute">
  <defs>
    <symbol id="i-home" viewBox="0 0 26 26"><circle cx="13" cy="13" r="13" fill="#fff"/><path d="M6 13.5 13 7l7 6.5h-2V19h-3.5v-4h-3v4H8v-5.5z" fill="#5c3310"/></symbol>
    <symbol id="i-phone" viewBox="0 0 26 26"><circle cx="13" cy="13" r="13" fill="#fff"/><path d="M9 6.5c.8-.4 1.5-.2 1.9.5l1.2 2.2c.3.7.1 1.3-.5 1.7l-.8.5c.6 1.6 1.8 2.9 3.3 3.6l.6-.8c.5-.6 1.1-.7 1.7-.4l2.1 1.3c.7.4.8 1.2.4 1.9-.8 1.3-2.2 1.9-3.7 1.4C10.9 17.1 8 14 7 10.4c-.4-1.5.5-3.2 2-3.9z" fill="#5c3310"/></symbol>
    <symbol id="i-mail" viewBox="0 0 26 26"><circle cx="13" cy="13" r="13" fill="#fff"/><rect x="6" y="8.5" width="14" height="9.5" rx="1" fill="#5c3310"/><path d="M6.5 9.2 13 14l6.5-4.8" fill="none" stroke="#fff" stroke-width="1.2"/></symbol>
    <symbol id="i-web" viewBox="0 0 26 26"><circle cx="13" cy="13" r="13" fill="#fff"/><circle cx="13" cy="13" r="7" fill="none" stroke="#5c3310" stroke-width="1.5"/><path d="M6 13h14M13 6c-3 3.5-3 10.5 0 14M13 6c3 3.5 3 10.5 0 14" fill="none" stroke="#5c3310" stroke-width="1.2"/></symbol>
    <symbol id="i-social" viewBox="0 0 26 26"><circle cx="13" cy="13" r="13" fill="#fff"/><circle cx="13" cy="13" r="5" fill="#5c3310"/></symbol>
  </defs>
</svg>

<main class="canvas">

  <!-- The Fine Print: outside -->
  <section class="card" style="left:34px;top:34px">
    <div class="back-panel">
      <div class="brand"><span class="brand-name">KASTON</span><span class="brand-tag">Fine Jewelry &amp; Custom Design</span></div>
      <ul class="contact-list">
        <li class="address"><svg><use href="#i-home"/></svg><span>Sandhollow Drive #9,<br>Cedarfield, VT 03871</span></li>
        <li><svg><use href="#i-phone"/></svg>603-555-0148</li>
        <li><svg><use href="#i-mail"/></svg>info@kastonjewelry.example</li>
        <li><svg><use href="#i-web"/></svg>www.kastonjewelry.example</li>
        <li><svg><use href="#i-social"/></svg>kastonjewelry</li>
        <li><svg><use href="#i-social"/></svg>kastonjewelry</li>
        <li><svg><use href="#i-social"/></svg>kastonjewelry</li>
        <li><svg><use href="#i-social"/></svg>kastonjewelry</li>
      </ul>
    </div>
    <div class="front-panel">
      <div class="brand"><span class="brand-name">KASTON</span><span class="brand-tag">Fine Jewelry &amp; Custom Design</span></div>
      <div class="title-band"><h2>The Fine Print</h2></div>
      <div class="jewel jewel-gold" role="img" aria-label="Photo of a gold swirl pendant with an orange garnet on a fine chain"></div>
    </div>
  </section>

  <!-- The Fine Print: inside -->
  <section class="card inside" style="left:34px;top:603px">
    <h3>We Want You To Love Your Jewelry!</h3>
    <p>We want you to be thrilled with your purchase from Kaston’s. That’s why we make it easy for you to return or exchange your purchase.</p>
    <p>Don’t forget, we’re here to help! If you didn’t get the jewelry of your dreams, let’s figure out what you really want.</p>
    <p>You may return your purchase from Kaston’s for a full refund within 2 weeks.</p>
    <p>You may exchange your purchase within 30 days for an item of equal value or you may opt to receive store credit.</p>
    <p>Returns must be in original condition.</p>
    <p>Merchandise that has been engraved, altered, sized or worn is non-returnable &amp; non-refundable.</p>
    <p>Custom jewelry and/or special orders are non-returnable &amp; non-refundable</p>
    <div class="sign"><span class="s-name">KASTON</span><span class="s-tag">Fine Jewelry &amp; Custom Design</span></div>
  </section>

  <!-- Our Guarantee: inside -->
  <section class="card inside inside-mini mini" style="left:780px;top:230px">
    <div class="lead-guarantee">
      <p>All new jewelry is guaranteed for one full year from the date of purchase.</p>
      <p>Any manufacturing defects found within that first year will be repaired or replaced at no charge.</p>
      <p>Simply bring the piece back to us with your receipt and we will be glad to help.</p>
    </div>
    <p>Our jewelry repairs are guaranteed for 6 months from completion date.</p>
    <p>Our watch repairs are guaranteed for 90 days from completion date. We do not warranty watches against water damage.</p>
    <p>We offer free lifetime cleaning and inspection of your jewelry from Kaston’s. We’ll make sure everything is safe &amp; secure and, of course, sparkling. You should do this at least every six months.</p>
    <p>Above all, we want you to be pleased with your jewelry purchase or repair from Kaston’s. If you have any questions or concerns, please never hesitate to speak to us.</p>
    <div class="sign"><span class="s-name">KASTON</span><span class="s-tag">Fine Jewelry &amp; Custom Design</span></div>
  </section>

  <!-- Our Guarantee: outside -->
  <section class="card mini" style="left:712px;top:34px">
    <div class="back-panel">
      <div class="brand"><span class="brand-name">KASTON</span><span class="brand-tag">Fine Jewelry &amp; Custom Design</span></div>
      <ul class="contact-list">
        <li class="address"><svg><use href="#i-home"/></svg><span>Sandhollow Drive #9,<br>Cedarfield, VT 03871</span></li>
        <li><svg><use href="#i-phone"/></svg>603-555-0148</li>
        <li><svg><use href="#i-mail"/></svg>info@kastonjewelry.example</li>
        <li><svg><use href="#i-web"/></svg>www.kastonjewelry.example</li>
        <li><svg><use href="#i-social"/></svg>kastonjewelry</li>
        <li><svg><use href="#i-social"/></svg>kastonjewelry</li>
        <li><svg><use href="#i-social"/></svg>kastonjewelry</li>
        <li><svg><use href="#i-social"/></svg>kastonjewelry</li>
      </ul>
    </div>
    <div class="front-panel">
      <div class="brand"><span class="brand-name">KASTON</span><span class="brand-tag">Fine Jewelry &amp; Custom Design</span></div>
      <div class="title-band"><h2>Our Guarantee</h2></div>
      <div class="jewel jewel-green" role="img" aria-label="Photo of a wide silver and gold ring set with three green tourmalines"></div>
    </div>
  </section>

  <!-- Layaway: inside -->
  <section class="card inside inside-mini mini" style="left:778px;top:793px">
    <div class="lead-layaway">
      <p>Layaway is available with 20% down and the balance paid in equal monthly installments over 90 days.</p>
      <p>Payments may be made in store, by phone or online at any time.</p>
      <p>No finance charges or fees.</p>
    </div>
    <p>A 5% restocking fee will be charged for layaways cancelled after 30 days.</p>
    <p>If your layaway is cancelled after 90 days, either by you or by us, all deposits &amp; payments will be converted to store credit. Restocking fee applies.</p>
    <p>Custom jewelry &amp; special orders placed on layaway require a 50% deposit and are non-cancellable &amp; non-refundable.</p>
    <p>Kaston’s retains the right to cancel any layaway, at any time, for late or inconsistent payments. Cancellation fees &amp; policies, as stated above, will apply.</p>
    <div class="sign"><span class="s-name">KASTON</span><span class="s-tag">Fine Jewelry &amp; Custom Design</span></div>
  </section>

  <!-- Layaway: outside -->
  <section class="card mini" style="left:711px;top:601px">
    <div class="back-panel">
      <div class="brand"><span class="brand-name">KASTON</span><span class="brand-tag">Fine Jewelry &amp; Custom Design</span></div>
      <ul class="contact-list">
        <li class="address"><svg><use href="#i-home"/></svg><span>Sandhollow Drive #9,<br>Cedarfield, VT 03871</span></li>
        <li><svg><use href="#i-phone"/></svg>603-555-0148</li>
        <li><svg><use href="#i-mail"/></svg>info@kastonjewelry.example</li>
        <li><svg><use href="#i-web"/></svg>www.kastonjewelry.example</li>
        <li><svg><use href="#i-social"/></svg>kastonjewelry</li>
        <li><svg><use href="#i-social"/></svg>kastonjewelry</li>
        <li><svg><use href="#i-social"/></svg>kastonjewelry</li>
        <li><svg><use href="#i-social"/></svg>kastonjewelry</li>
      </ul>
    </div>
    <div class="front-panel">
      <div class="brand"><span class="brand-name">KASTON</span><span class="brand-tag">Fine Jewelry &amp; Custom Design</span></div>
      <div class="title-band"><h2>Layaway</h2></div>
      <div class="jewel jewel-quartz" role="img" aria-label="Photo of a pendant with a square rutilated quartz above a black onyx point on a gold chain"></div>
    </div>
  </section>

</main>
</body>
</html>
```